" Leia o briefing antes de produzir, as informações contidas são FUNDAMENTAIS para o desenvolvimento das peças. - É uma creche que atua com bebês e crianças até 5 anos. "

```html
<!DOCTYPE html>
<html lang="pt-BR">
<head>
<meta charset="utf-8">
<title>Roda Encantada – Fachada</title>
<link href="https://fonts.googleapis.com/css2?family=Varela+Round&display=swap" rel="stylesheet">
<style>
  :root {
    --lime: #c5d500;
    --leaf-dark: #4f8a1e;
    --leaf-light: #a9d44a;
    --sky-blue: #0a9be0;
    --brand-blue: #1c5fa8;
    --white: #ffffff;
    --grey-light: #b4b4b4;
    --grey-mid: #8a8a8a;
    --grey-dark: #4a4a4a;
    --grey-base: #c9c9c9;
  }
  html, body {
    margin: 0;
    padding: 0;
    width: 1200px;
    height: 1200px;
    overflow: hidden;
    background: var(--white);
  }
  .facade {
    position: relative;
    width: 1200px;
    height: 1200px;
    overflow: hidden;
    font-family: "Varela Round", "Nunito", sans-serif;
  }
  .tree-canopy {
    position: absolute;
    left: 0; top: 0;
    width: 1200px; height: 204px;
    background: linear-gradient(180deg, var(--leaf-light) 0%, #7fb832 50%, var(--leaf-dark) 100%);
  }
  .sign-band {
    position: absolute;
    left: 0; top: 204px;
    width: 1200px; height: 312px;
    background: var(--lime);
  }
  .brand-badge {
    position: absolute;
    left: 396px; top: 48px;
    width: 408px; height: 408px;
    border-radius: 50%;
    background: var(--white);
    display: flex;
    align-items: center;
    justify-content: center;
    text-align: center;
  }
  .brand-name {
    color: var(--brand-blue);
    font-size: 62px;
    line-height: 1.1;
  }
  .tagline {
    position: absolute;
    left: 12px; top: 64px;
    width: 330px;
    color: var(--white);
    font-size: 35px;
    line-height: 50px;
    text-align: center;
    margin: 0;
  }
  .activities {
    position: absolute;
    left: 810px; top: 60px;
    margin: 0; padding: 0;
    list-style: none;
    color: var(--white);
    font-size: 31px;
    line-height: 52px;
    white-space: nowrap;
  }
  .activities span { margin-right: 14px; }
  .activities span:last-child { margin-right: 0; }
  .blue-band {
    position: absolute;
    left: 0; top: 516px;
    width: 1200px; height: 84px;
    background: var(--sky-blue);
  }
  .color-mosaic {
    position: absolute;
    left: 0; top: 600px;
    width: 1200px; height: 384px;
    background: linear-gradient(100deg, #e4586f 0%, #ffd21a 22%, #1e8fd6 40%, #e8262d 55%, #7b4fa3 72%, #b7d433 86%, #1e8fd6 100%);
  }
  .base {
    position: absolute;
    left: 0;
    width: 1200px;
  }
  .base--light { top: 984px; height: 84px; background: var(--grey-light); }
  .base--mid   { top: 1068px; height: 24px; background: var(--grey-mid); }
  .base--dark  { top: 1092px; height: 41px; background: var(--grey-dark); }
  .base--floor { top: 1133px; height: 67px; background: var(--grey-base); }
</style>
</head>
<body>
  <main class="facade">
    <div class="tree-canopy" role="img" aria-label="Foto de copas de árvores verdes ao sol"></div>

    <section class="sign-band">
      <p class="tagline">“Era uma vez......<br>o mundo mágico<br>da fantasia!”</p>
      <ul class="activities">
        <li><span>Circo</span><span>Teatro</span><span>Música</span></li>
        <li><span>Culinária</span><span>Horticultura</span></li>
        <li><span>Passeios</span><span>Artes</span><span>Mágica</span></li>
      </ul>
    </section>

    <div class="brand-badge">
      <span class="brand-name">Roda<br>Encantada</span>
    </div>

    <div class="blue-band"></div>

    <div class="color-mosaic" role="img" aria-label="Mosaico geométrico de triângulos coloridos com linhas brancas"></div>

    <div class="base base--light"></div>
    <div class="base base--mid"></div>
    <div class="base base--dark"></div>
    <div class="base base--floor"></div>
  </main>
</body>
</html>
```